Verpackung für Hanf-Nudeln gesucht
Zielgruppe
Wir haben Hanf & Natur Shops und Onlineshop. Zielgruppe sind Menschen die gesund und bewusst Leben möchten.
Aufgabenstellung
Verpackung für Hanf-Nudeln (Suppen-, Band-, Spaghetti-, Hörnchennudeln). 500g abgepackt.
Wichtig: handgemacht in Österreich, 100 % vegan und bio
sie enthalten Dinkel- und Hanfmehl sowie geringe Mengen an Kelmin STEINPERLE und werden mit nitratfreiem Wasser erzeugt. Die Hanfnudeln sind vollkommen frei von synthetischen Hilfsmitteln. Kochzeit ca. 3 Minuten., Info für alle Allergiker, Hanfnudeln sind NICHT GLUTENFREI., Zutaten: Dinkel, Hanfmehl, Steinsalz, nitratfreies Wasser
Verpackungsvorschläge bitte
Modernes Design, passend zu unseren anderen Voltaruna Produkten

```html
<!DOCTYPE html>
<html lang="de">
<head>
<meta charset="utf-8">
<title>Voltaruna Hörnchen Nudeln – Verpackung</title>
<link rel="stylesheet" href="https://fonts.googleapis.com/css2?family=Montserrat:wght@400;600;900&family=Mr+Dafoe&display=swap">
<style>
  :root {
    --stage: #ffffff;
    --film: #eef0ea;
    --pasta-light: #e3cf70;
    --pasta-dark: #c2ad45;
    --hemp-green: #b6dd3f;
    --label-green: #a4d23a;
    --kraft: #c6aa8d;
    --kraft-dark: #b89a7c;
    --brand-ink: #3d4a45;
    --white: #ffffff;
  }
  * { margin: 0; padding: 0; box-sizing: border-box; }
  html, body {
    width: 1200px; height: 900px; overflow: hidden;
    background: var(--stage);
    font-family: "Montserrat", sans-serif;
  }
  .package {
    position: absolute; left: 360px; top: 100px;
    width: 480px; height: 700px;
  }
  .package-art { position: absolute; inset: 0; }
  .brand {
    position: absolute; left: 0; right: 0; top: 168px;
    display: flex; justify-content: center; align-items: center; gap: 10px;
    color: var(--brand-ink);
    font-weight: 600; font-size: 22px; letter-spacing: 1px;
  }
  .brand-dot {
    width: 14px; height: 14px; border-radius: 50%;
    background: var(--brand-ink);
  }
  .variety {
    position: absolute; left: 80px; top: 380px; width: 340px;
    text-align: center;
    font-family: "Mr Dafoe", cursive;
    font-size: 84px; color: var(--label-green);
    transform: rotate(-22deg);
    line-height: 1;
  }
  .product-name {
    position: absolute; left: 0; right: 0; top: 455px;
    text-align: center; color: var(--white);
    font-weight: 900; font-size: 58px; letter-spacing: 1px;
  }
  .origin {
    position: absolute; left: 0; right: 0; top: 521px;
    text-align: center; color: var(--white);
    font-size: 11.5px; letter-spacing: 2.4px;
  }
  .claims {
    position: absolute; left: 0; right: 0; top: 566px;
    display: flex; flex-direction: column; align-items: center; gap: 6px;
  }
  .claim {
    width: 104px; height: 21px; line-height: 21px;
    background: var(--label-green); color: var(--white);
    text-align: center; font-size: 12.5px; letter-spacing: 1.2px;
  }
  .net-weight {
    position: absolute; left: 0; right: 0; top: 642px;
    text-align: center; color: var(--white);
    font-weight: 600; font-size: 11px; letter-spacing: 1.5px;
  }
</style>
</head>
<body>
<main class="package">
  <svg class="package-art" viewBox="0 0 480 700" width="480" height="700">
    <defs>
      <linearGradient id="pasta-tone" x1="0" y1="0" x2="1" y2="1">
        <stop offset="0" stop-color="var(--pasta-light)"/>
        <stop offset="1" stop-color="var(--pasta-dark)"/>
      </linearGradient>
    </defs>
    <rect class="bag-film" x="0" y="0" width="480" height="700" fill="var(--film)"/>
    <rect class="pasta-window" x="60" y="85" width="360" height="440" rx="20"
          fill="url(#pasta-tone)" role="img" aria-label="Hörnchennudeln durch das Sichtfenster"/>
    <path class="hemp-band" d="M112 0 H480 V270 Q400 330 290 300 Q190 270 150 180 Q125 110 112 0 Z"
          fill="var(--hemp-green)" opacity="0.6"/>
    <g class="top-seal" stroke="#ffffff" stroke-opacity="0.7" stroke-width="1.5">
      <line x1="0" y1="10" x2="480" y2="10"/><line x1="0" y1="18" x2="480" y2="18"/>
      <line x1="0" y1="26" x2="480" y2="26"/><line x1="0" y1="34" x2="480" y2="34"/>
    </g>
    <path class="kraft-panel" d="M0 480 Q60 470 120 460 Q220 440 330 415 Q420 395 480 385 V700 H0 Z"
          fill="var(--kraft)" role="img" aria-label="Kraftpapier-Fläche"/>
    <g class="bottom-seal" stroke="var(--kraft-dark)" stroke-width="1.5">
      <line x1="0" y1="668" x2="480" y2="668"/><line x1="0" y1="676" x2="480" y2="676"/>
      <line x1="0" y1="684" x2="480" y2="684"/><line x1="0" y1="692" x2="480" y2="692"/>
    </g>
  </svg>

  <div class="brand"><span class="brand-dot"></span><span class="brand-name">VOLTARUNA</span></div>
  <div class="variety">Hörnchen</div>
  <h1 class="product-name">NUDELN</h1>
  <p class="origin">HANDGEMACHT IN ÖSTERREICH</p>
  <div class="claims">
    <span class="claim">100 % vegan</span>
    <span class="claim">100 % bio</span>
  </div>
  <p class="net-weight">500 g</p>
</main>
</body>
</html>
```